Re-design of current business cards

We are updating our website with new colors and layout. Would like to re-design our business cards to co-ordinate. See attached pdf with new Brindlecraft website colors. We would also like to combine our 2 brands on the one business card. Attached is the new design for our Brindlecraft website, current business cards, which are one sided, brindlecraft logo in tiff, .ai for fonts. Brindlecraft logo font is Optimum, Quillmarsh website home page image, Quillmarsh brand statics for products which includes the logo for this brand.

Quillmarsh brand will stay the dark gray on the website. See attached statics for product and website home page.
Updates

The business cards will be 2 sided. Brindlecraft Brand on one side and Quillmarsh Brand on the other. The colors for Brindlecraft need to follow the color scheme of the brindlecraft website pdf I uploaded. The colors are a blue, lighter teal blue and white. Quillmarsh needs to follow the dark gray color on files uploaded

Target Market(s)

The trade and consumers

Industry/Entity Type

Home Furnishing

Contact Information for Business Card

We are updating our website with new colors and layout. Would like to re-design our business cards to co-ordinate. We would also like to combine our 2 brands onto 1 2 sided business cards.

Requirements
Must have
• Colors that match our new website, see attached image.
• RGB colors
• navy -#152842
• teal - 98aeb9
• The gray color used for Quillmarsh brands.
• ll logos and fonts should stay the same.

```html
<!DOCTYPE html>
<html lang="en">
<head>
<meta charset="utf-8">
<title>Brindlecraft and Quillmarsh Business Card</title>
<link rel="stylesheet" href="https://fonts.googleapis.com/css2?family=Tenor+Sans&family=PT+Sans:wght@400&display=swap">
<style>
  :root {
    --navy: #152842;
    --teal: #98aeb9;
    --mark: #6d8579;
    --quill-gray: #4a4a4a;
    --paper: #ffffff;
    --ink: #151515;
    --backdrop: #c9c8c4;
  }
  html, body { margin: 0; padding: 0; }
  body {
    width: 1039px; height: 1200px; overflow: hidden;
    background: var(--backdrop); position: relative;
  }
  .card { position: absolute; width: 961px; height: 549px; overflow: hidden; }
  .card-front { left: 35px; top: 57px; background: var(--paper); }
  .card-back { left: 36px; top: 616px; background: var(--navy); }
  .card-shapes { position: absolute; inset: 0; }

  .brand-dot { position: absolute; border-radius: 50%; }
  .brand-name, .brand-url {
    position: absolute; margin: 0; white-space: nowrap; text-align: center;
    font-family: "Tenor Sans", sans-serif; font-weight: 400;
  }

  .card-front .brand-dot { left: 174px; top: 145px; width: 82px; height: 82px; background: var(--mark); }
  .card-front .brand-name { left: 0; width: 434px; top: 236px; font-size: 45px; line-height: 1; color: var(--ink); letter-spacing: 1px; }
  .card-front .brand-url { left: 0; width: 434px; top: 287px; font-size: 19px; line-height: 1; color: var(--ink); letter-spacing: 1px; }

  .holder-name {
    position: absolute; left: 390px; width: 486px; top: 86px; margin: 0; text-align: center; white-space: nowrap;
    font-family: "Tenor Sans", sans-serif; font-size: 31px; line-height: 1; font-weight: 400;
    color: var(--navy); letter-spacing: 0.5px; -webkit-text-stroke: 0.9px var(--navy);
  }
  .holder-title {
    position: absolute; left: 390px; width: 486px; top: 130px; margin: 0; text-align: center; white-space: nowrap;
    font-family: "Tenor Sans", sans-serif; font-size: 20px; line-height: 1; color: var(--teal);
  }
  .contact {
    position: absolute; left: 526px; top: 226px; margin: 0; padding: 0 0 0 13px;
    border-left: 5px solid var(--navy); list-style: none; white-space: nowrap;
    font-family: "PT Sans", sans-serif; font-size: 21px; color: var(--navy);
  }
  .contact li { height: 55px; line-height: 26px; }
  .contact li:last-child { height: 26px; }

  .card-back .brand-dot { left: 489px; top: 96px; width: 133px; height: 133px; background: var(--quill-gray); }
  .card-back .brand-name { left: 208px; width: 700px; top: 244px; font-size: 76px; line-height: 1; color: var(--paper); letter-spacing: 1px; }
  .card-back .brand-url { left: 208px; width: 700px; top: 318px; font-size: 30px; line-height: 1; color: var(--paper); letter-spacing: 1.5px; }
</style>
</head>
<body>
  <section class="card card-front" aria-label="Brindlecraft side">
    <svg class="card-shapes" width="961" height="549" viewBox="0 0 961 549" aria-hidden="true">
      <rect x="0" y="518" width="961" height="31" fill="var(--navy)"/>
      <polygon points="432,549 514,481 961,484 961,549" fill="var(--teal)"/>
    </svg>
    <span class="brand-dot" aria-hidden="true"></span>
    <p class="brand-name">BRINDLECRAFT</p>
    <p class="brand-url">www.brindlecraft.com</p>
    <h1 class="holder-name">MAREN HOLLOWAY</h1>
    <p class="holder-title">GRAPHICS/PHOTOGRAPHY DIRECTOR</p>
    <ul class="contact">
      <li>P.O.BOX 214/1870 FERNBROOK RIDGE RD</li>
      <li>ALDER FALLS, VIRGINIA 24099</li>
      <li>P 555.014.2271</li>
      <li>F 555.014.2289</li>
      <li>EMAIL: mholloway@brindlecraft.com</li>
    </ul>
  </section>

  <section class="card card-back" aria-label="Quillmarsh side">
    <svg class="card-shapes" width="961" height="549" viewBox="0 0 961 549" aria-hidden="true">
      <polygon points="418,0 961,0 961,549 597,549" fill="var(--teal)"/>
    </svg>
    <span class="brand-dot" aria-hidden="true"></span>
    <p class="brand-name">QUILLMARSH</p>
    <p class="brand-url">www.quillmarsh.com</p>
  </section>
</body>
</html>
```